Australian Painting company requires DL Flyer to help grow business

We need a flyer to post, email and leave with clients which details our company information and identifies the services we provide

Needs to incorporate our existing logo and show photos which will be provided when basic layout and designer is chosen

my mistake for not making the brief clear earlier; I would like an A4 double sided flyer which folds to DL

Target Market(s)

property managers, facility managers, property owners

Industry/Entity Type

Business

Requirements
Must have
• Company Name - Bellwick Paintworks Australia
Phone Number - 1300 842 306
Web Address - www.bpwks.com.au
Email: admin@bpwks.com.au
Facebook symbol
Twitter symbol
Logo - Attached to brief
Description of services;
◾External Painting
◾Internal Painting
◾Texture Coating
◾Two Pak Epoxy products
◾Line marking
◾Epoxy floors and walkways
◾Waterproofing
◾Roof Painting
◾Handyman Services
◾Rope Access Painting
◾Maintenance Programmes
◾Painting Project Management
◾Prestigious Home Painting
Nice to have
• Photos of some projects; some photos are attached
can provide more when a design is selected
Should not have
• Too much information - needs to be easy to read

```html
<!DOCTYPE html>
<html lang="en">
<head>
<meta charset="utf-8">
<title>Bellwick Paintworks Australia – Standards</title>
<link href="https://fonts.googleapis.com/css2?family=Open+Sans:wght@300;400;700&display=swap" rel="stylesheet">
<style>
  :root {
    --black: #000000;
    --white: #ffffff;
    --blue-deep: #0b3f9a;
    --blue-mid: #1565c0;
    --blue-brand: #1a5fc4;
    --blue-bright: #1e9be0;
    --blue-sky: #29a9e8;
    --photo-blue: #24449a;
    --photo-grey: #c4c8d0;
    --photo-light: #e4e6ea;
  }
  * { margin: 0; padding: 0; box-sizing: border-box; }
  html, body { width: 1200px; height: 848px; overflow: hidden; background: var(--white); }
  .flyer-page {
    position: relative;
    width: 1200px;
    height: 848px;
    overflow: hidden;
    background: var(--black);
    font-family: "Open Sans", Arial, sans-serif;
    color: var(--white);
  }
  .flyer-art { position: absolute; inset: 0; }
  .label-before {
    position: absolute; left: 113px; top: 11px;
    font-size: 13px; font-weight: 700; color: var(--black);
  }
  .label-after {
    position: absolute; left: 127px; top: 453px;
    font-size: 28px; font-weight: 700; color: var(--black);
  }
  .section-title {
    position: absolute; left: 62px; top: 600px;
    font-size: 41px; font-weight: 300; letter-spacing: 0.3px;
  }
  .standards-intro {
    position: absolute; left: 364px; top: 595px;
    white-space: nowrap;
    font-size: 20.5px; line-height: 28px; font-weight: 400;
  }
  .site-rules {
    position: absolute; left: 724px; top: 577px; width: 300px;
    list-style: none; font-size: 13.5px; line-height: 18px;
  }
  .site-rules li { margin-bottom: 20px; }
  .brand-name {
    position: absolute; left: 1064px; top: 449px;
    writing-mode: vertical-rl;
    white-space: nowrap;
    font-size: 16px; font-weight: 400; letter-spacing: 3.2px; color: var(--white);
  }
  .brand-mark {
    position: absolute; left: 1102px; top: 447px;
    writing-mode: vertical-rl;
    white-space: nowrap;
    font-size: 64px; line-height: 72px; font-weight: 700; letter-spacing: 3px; color: var(--blue-brand);
  }
</style>
</head>
<body>
<main class="flyer-page">
  <svg class="flyer-art" width="1200" height="848" viewBox="0 0 1200 848" xmlns="http://www.w3.org/2000/svg">
    <defs>
      <linearGradient id="photoTone" x1="0" y1="0" x2="0.35" y2="1">
        <stop offset="0" stop-color="var(--photo-grey)"/>
        <stop offset="0.18" stop-color="#8a96b8"/>
        <stop offset="0.32" stop-color="var(--photo-blue)"/>
        <stop offset="0.5" stop-color="#3a5aa8"/>
        <stop offset="0.62" stop-color="var(--photo-blue)"/>
        <stop offset="0.75" stop-color="#b9bfcc"/>
        <stop offset="1" stop-color="var(--photo-light)"/>
      </linearGradient>
      <linearGradient id="insetTone" x1="0" y1="0" x2="0" y2="1">
        <stop offset="0" stop-color="#dfe3ea"/>
        <stop offset="0.6" stop-color="#9fb7cc"/>
        <stop offset="1" stop-color="#4f7ea8"/>
      </linearGradient>
      <linearGradient id="panelTone" x1="0" y1="0" x2="0" y2="1">
        <stop offset="0" stop-color="var(--blue-sky)"/>
        <stop offset="1" stop-color="#1386d2"/>
      </linearGradient>
    </defs>

    <rect class="project-photo" x="0" y="0" width="1033" height="580" fill="url(#photoTone)" role="img" aria-label="Photo of a repainted sports centre ceiling with blue ducting and white steel trusses"/>

    <rect x="38" y="34" width="233" height="152" fill="var(--black)"/>
    <rect class="before-photo" x="44" y="40" width="221" height="140" fill="url(#insetTone)" role="img" aria-label="Photo of the same sports centre interior before repainting"/>

    <path class="lower-field" d="M0,515 C320,610 720,575 1200,365 L1200,848 L0,848 Z" fill="var(--black)"/>
    <path class="side-panel" d="M0,515 C120,552 230,572 342,582 L342,848 L0,848 Z" fill="url(#panelTone)"/>

    <path class="wave wave-bright" d="M0,448 C330,560 760,520 1200,338 L1200,352 C760,535 330,575 0,462 Z" fill="var(--blue-bright)"/>
    <path class="wave wave-deep" d="M0,462 C330,575 760,535 1200,352 L1200,374 C760,560 330,598 0,495 Z" fill="var(--blue-deep)"/>
    <path class="wave wave-mid" d="M0,495 C330,598 760,560 1200,374 L1200,384 C760,572 330,612 0,515 Z" fill="var(--blue-mid)"/>
  </svg>

  <span class="label-before">BEFORE</span>
  <span class="label-after">AFTER</span>

  <h2 class="section-title">STANDARDS:</h2>
  <p class="standards-intro">With years of trade experience<br>we know only too well the type<br>of disruption which can be<br>caused by a major repainting<br>project; in order to minimise<br>such problems our painters<br>operate under the following<br>code of conduct and site rules:</p>

  <ul class="site-rules">
    <li>Our painters are in uniform<br>at all times</li>
    <li>Strictly no smoking on site</li>
    <li>No radios on site</li>
    <li>Drop sheets are used at all times</li>
    <li>Wet Paint signs and barricades<br>are used to protect the public</li>
    <li>No washing of equipment on site</li>
  </ul>

  <span class="brand-name">BELLWICK PAINTWORKS AUSTRALIA</span>
  <span class="brand-mark">BELLWICK</span>
</main>
</body>
</html>
```